Loyalty/Gift Card Design-

Pumlavo needs a design for a loyalty card for a retail gas discount program. The card will need to fit specifications for brenvoxa cards cr-80 magnetic card found on www.brenvoxa.com

The way our program works is a consumer will see advertisement for our program and come to a local gas station to purchase our Pumlavo Card. It will be a set price up- front, then our program/card will save consumers 15 cents per gallon on 100 gallons of fuel. Once the 100 gallons is used the customer will have the option of reloading (for another set cost) another 100 gallons on the card to receive another 15 cents off on next 100 gallons.

Key Info to Incorporate on card--
"Save 15 cents per gallon on next 100 gallons of fuel"
Never pay full price on fuel again!
"Card Valid Only At" (then a space for our stores name and address)
Brought to you by-- Pumlavo Name & Logo

Target Market(s)

Consumers conscious of gas prices/ economy who are looking to save money where they can. We are looking for a design that fits "big box" theme, with very clean design.

Industry/Entity Type

Gas Station

Requirements
Must have
• Colors Red,, Blue, White--
Sell Message of Saving and Value.
Should not have
• Designs with fuel pumps

```html
<!DOCTYPE html>
<html lang="en">
<head>
<meta charset="utf-8">
<title>Pumlavo Fuel Card</title>
<link rel="stylesheet" href="https://fonts.googleapis.com/css2?family=Open+Sans:wght@400;600&family=Ubuntu:wght@500;700&display=swap">
<style>
  :root {
    --page: #ffffff;
    --card-blue: #4757f2;
    --ray-light: #5566f7;
    --ray-dark: #3e4de8;
    --brand-navy: #1f2a9c;
    --accent-red: #d40d0d;
    --headline-outline: #3a0000;
    --text-white: #ffffff;
    --band-white: #ffffff;
    --band-text: #111111;
    --photo-top: #c9a27c;
    --photo-mid: #9fdcef;
    --photo-low: #7fc6e0;
  }
  * { margin: 0; padding: 0; box-sizing: border-box; }
  html, body {
    width: 1200px; height: 800px; overflow: hidden;
    background: var(--page);
  }
  .canvas { position: relative; width: 1200px; height: 800px; }
  .fuel-card {
    position: absolute; left: 34px; top: 43px;
    width: 1149px; height: 714px;
    border-radius: 40px; overflow: hidden;
    background:
      repeating-conic-gradient(from 0deg at 84% 44%,
        var(--ray-light) 0deg 7deg, var(--ray-dark) 7deg 16deg),
      var(--card-blue);
  }
  .brand-mark {
    position: absolute; left: 60px; top: 70px;
    display: flex; align-items: center; gap: 26px;
  }
  .brand-mark__square {
    width: 150px; height: 150px; background: var(--brand-navy);
    border-radius: 18px;
  }
  .brand-mark__name {
    font-family: "Ubuntu", sans-serif; font-weight: 700;
    font-size: 112px; color: var(--brand-navy); letter-spacing: 1px;
  }
  .product-line {
    position: absolute; left: 657px; top: 230px;
    font-family: "Open Sans", sans-serif; font-size: 22px;
    color: var(--accent-red); letter-spacing: 1px;
  }
  .offer-quote {
    position: absolute; left: 37px; top: 328px;
    font-family: "Open Sans", sans-serif; font-weight: 400;
    font-size: 25px; color: var(--text-white);
  }
  .headline {
    position: absolute; left: 126px; top: 368px;
    font-family: "Ubuntu", sans-serif; font-weight: 700;
    font-size: 35px; color: var(--accent-red);
    -webkit-text-stroke: 1px var(--headline-outline);
  }
  .valid-at {
    position: absolute; left: 37px; top: 438px;
    font-family: "Open Sans", sans-serif; font-size: 25px;
    color: var(--text-white);
  }
  .spokesperson-photo {
    position: absolute; left: 800px; top: 81px;
    width: 310px; height: 633px;
    border-radius: 120px 120px 0 0;
    background: linear-gradient(180deg, var(--photo-top) 0%, var(--photo-top) 30%, var(--photo-mid) 45%, var(--photo-low) 100%);
  }
  .sponsor-band {
    position: absolute; left: 0; top: 605px;
    width: 100%; height: 64px;
    background: var(--band-white);
    display: flex; align-items: center;
    padding-left: 20px;
  }
  .sponsor-band__label {
    font-family: "Open Sans", sans-serif; font-weight: 600;
    font-size: 25px; color: var(--band-text);
  }
  .sponsor-band__name {
    margin-left: 38px;
    font-family: "Open Sans", sans-serif; font-weight: 600;
    font-size: 26px; color: var(--brand-navy);
  }
  .band-mark {
    position: absolute; left: 692px; top: 582px;
    display: flex; align-items: center; gap: 14px;
  }
  .band-mark__square {
    width: 76px; height: 76px; background: var(--brand-navy);
    border-radius: 10px;
  }
  .band-mark__name {
    font-family: "Ubuntu", sans-serif; font-weight: 700;
    font-size: 54px; color: var(--brand-navy);
  }
</style>
</head>
<body>
<div class="canvas">
  <div class="fuel-card">
    <div class="brand-mark">
      <span class="brand-mark__square"></span>
      <span class="brand-mark__name">Pumlavo</span>
    </div>
    <div class="product-line">FUEL CARDS</div>

    <p class="offer-quote">"Save 15 cents per gallon on next 100 gallons of fuel"</p>
    <p class="headline">Never pay full price on fuel again!</p>
    <p class="valid-at">Card Valid Only At :</p>

    <div class="spokesperson-photo" role="img" aria-label="Photo of a smiling spokeswoman in a light blue top"></div>

    <div class="sponsor-band">
      <span class="sponsor-band__label">Brought to you by :</span>
      <span class="sponsor-band__name">Pumlavo</span>
    </div>
    <div class="band-mark">
      <span class="band-mark__square"></span>
      <span class="band-mark__name">Pumlavo</span>
    </div>
  </div>
</div>
</body>
</html>
```